Want a DL Flyer designed for mailout, with the following info. Please see the website www.ledgerbrightco.com.au for any other info.
Content:
EVERYTHING YOU NEED FROM AN ACCOUNTANT
(tick) Value for money
(tick) Mobile visits to your farm or business
(tick) Fixed Fees Agreed Upfront
(tick) Advice tailored to your circumstances
(tick) Help to grow your business
(tick) Talk directly to your accountant, the person who knows you
(tick) Small business & Primary Producer Specialists
+ MORE.......TALLYWELL GROUP. YOU'RE MORE THAN A NUMBER WITH US.
Director: Gordon Pellew CPA | Associate: Soraya Finch CPA
Call (07) 4519 2386 www.ledgerbrightco.com.au PO Box 827 Wandarra Qld 4417

```html
<!DOCTYPE html>
<html lang="en">
<head>
<meta charset="utf-8">
<title>Tallywell Group – DL Flyer</title>
<link rel="stylesheet" href="https://fonts.googleapis.com/css2?family=Bebas+Neue&family=Montserrat:wght@600;700;800&family=Roboto:wght@400;500;700&display=swap">
<style>
  :root {
    --backdrop: #424242;
    --red: #e01e1e;
    --ink: #1b1b1b;
    --white: #ffffff;
    --photo-a: #6f86a8;
    --photo-b: #c9d3df;
  }
  * { box-sizing: border-box; margin: 0; padding: 0; }
  html, body { width: 1200px; height: 1200px; overflow: hidden; }
  body { background: var(--backdrop); position: relative; font-family: "Roboto", sans-serif; }

  .flyer { position: absolute; top: 184px; width: 405px; height: 834px; overflow: hidden; }
  .flyer--front { left: 136px; background: var(--white); }
  .flyer--back { left: 661px; background: var(--ink); }
  .flyer svg.shapes { position: absolute; inset: 0; width: 405px; height: 834px; }

  .brand { position: absolute; display: flex; align-items: center; gap: 10px;
           font-family: "Montserrat", sans-serif; font-weight: 700; white-space: nowrap; }
  .brand__mark { width: 22px; height: 22px; }
  .brand--front { top: 112px; left: 0; width: 405px; justify-content: center; font-size: 31px; line-height: 40px; color: var(--red); }
  .brand--front .brand__mark { background: var(--red); }
  .brand--back { top: 76px; right: 24px; font-size: 22px; line-height: 28px; color: var(--white); }
  .brand--back .brand__mark { background: var(--white); width: 18px; height: 18px; }

  .front__headline { position: absolute; left: 24px; top: 660px; font-family: "Bebas Neue", sans-serif;
                     font-size: 64px; line-height: 1; color: var(--red); }
  .front__sub { position: absolute; left: 24px; top: 714px; font-family: "Montserrat", sans-serif;
                font-weight: 800; font-size: 23.5px; line-height: 28px; color: var(--white); }
  .front__call { position: absolute; left: 0; width: 405px; top: 755px; text-align: center;
                 font-family: "Montserrat", sans-serif; font-weight: 700; font-size: 24px; line-height: 30px; color: var(--white); }
  .front__call .label { color: var(--red); }
  .web { display: flex; align-items: center; gap: 8px; font-family: "Montserrat", sans-serif;
         font-weight: 600; font-size: 14.5px; line-height: 20px; color: var(--white); }
  .front__web { position: absolute; left: 0; width: 405px; top: 792px; justify-content: center; }

  .back__content { position: absolute; left: 23px; top: 140px; width: 362px; color: var(--white); }
  .back__heading { font-weight: 700; font-size: 24.5px; line-height: 26px; color: var(--red); text-transform: uppercase; }
  .benefits { list-style: none; margin-top: 10px; }
  .benefits li { position: relative; padding-left: 25px; font-size: 16.4px; line-height: 20px; margin-bottom: 10px; }
  .benefits li svg { position: absolute; left: 0; top: 2px; width: 16px; height: 16px; }
  .back__tagline { font-weight: 700; font-size: 23px; line-height: 28px; text-transform: uppercase; margin-top: 0; }
  .team { margin-top: 9px; font-size: 24.5px; line-height: 30px; }
  .team .role { color: var(--red); font-weight: 500; }
  .back__phone { display: flex; align-items: center; gap: 10px; margin-top: 11px;
                 font-family: "Montserrat", sans-serif; font-weight: 700; font-size: 28px; line-height: 34px; }
  .contact-line { display: flex; align-items: center; gap: 10px; font-size: 16.4px; line-height: 20px; margin-top: 10px; }
  .back__web { margin-top: 9px; font-family: "Roboto", sans-serif; font-weight: 500; font-size: 16.4px; gap: 10px; }
</style>
</head>
<body>

<section class="flyer flyer--front">
  <svg class="shapes" viewBox="0 0 405 834">
    <defs>
      <linearGradient id="photoTone" x1="0" y1="0" x2="1" y2="1">
        <stop offset="0" stop-color="var(--photo-a)"/>
        <stop offset="0.55" stop-color="var(--photo-b)"/>
        <stop offset="1" stop-color="#7a8aa0"/>
      </linearGradient>
    </defs>
    <rect x="0" y="130" width="405" height="530" fill="url(#photoTone)" role="img"
          aria-label="Photo: businesswoman shaking hands with a client in front of an office building"/>
    <path d="M0,0 H405 V156 Q202,225 0,158 Z" fill="var(--red)"/>
    <path d="M0,0 H405 V132 Q202,240 0,136 Z" fill="var(--white)"/>
    <path d="M0,636 Q200,584 405,612 V834 H0 Z" fill="var(--red)"/>
    <path d="M0,648 Q300,602 405,752 V834 H0 Z" fill="var(--ink)"/>
  </svg>

  <div class="brand brand--front"><span class="brand__mark"></span>Tallywell Group</div>

  <h1 class="front__headline">YOU ARE NOT</h1>
  <p class="front__sub">JUST A NUMBER WITH US</p>
  <p class="front__call"><span class="label">Call</span> (07) 4519 2386</p>
  <p class="web front__web">
    <svg width="13" height="13" viewBox="0 0 24 24" fill="none" stroke="var(--red)" stroke-width="2"><circle cx="12" cy="12" r="10"/><path d="M2 12h20M12 2c3 3 3 17 0 20M12 2c-3 3-3 17 0 20"/></svg>
    www.ledgerbrightco.com.au
  </p>
</section>

<section class="flyer flyer--back">
  <svg class="shapes" viewBox="0 0 405 834">
    <path d="M0,0 H295 Q160,90 0,134 Z" fill="var(--red)"/>
    <path d="M0,0 H99 Q50,40 0,80 Z" fill="var(--white)"/>
    <path d="M0,700 Q200,790 405,676 V834 H0 Z" fill="var(--red)"/>
    <path d="M0,718 Q260,860 405,796 V834 H0 Z" fill="var(--white)"/>
  </svg>

  <div class="brand brand--back"><span class="brand__mark"></span>Tallywell Group</div>

  <div class="back__content">
    <h2 class="back__heading">Everything you need from<br>an accountant</h2>
    <ul class="benefits">
      <li><svg viewBox="0 0 16 16"><circle cx="8" cy="8" r="8" fill="var(--red)"/><path d="M4.5 8.3l2.4 2.3 4.6-4.8" stroke="#fff" stroke-width="1.8" fill="none"/></svg>Value for money</li>
      <li><svg viewBox="0 0 16 16"><circle cx="8" cy="8" r="8" fill="var(--red)"/><path d="M4.5 8.3l2.4 2.3 4.6-4.8" stroke="#fff" stroke-width="1.8" fill="none"/></svg>Mobile visits to your farm or business</li>
      <li><svg viewBox="0 0 16 16"><circle cx="8" cy="8" r="8" fill="var(--red)"/><path d="M4.5 8.3l2.4 2.3 4.6-4.8" stroke="#fff" stroke-width="1.8" fill="none"/></svg>Fixed Fees Agreed Upfront</li>
      <li><svg viewBox="0 0 16 16"><circle cx="8" cy="8" r="8" fill="var(--red)"/><path d="M4.5 8.3l2.4 2.3 4.6-4.8" stroke="#fff" stroke-width="1.8" fill="none"/></svg>Advice tailored to your circumstances</li>
      <li><svg viewBox="0 0 16 16"><circle cx="8" cy="8" r="8" fill="var(--red)"/><path d="M4.5 8.3l2.4 2.3 4.6-4.8" stroke="#fff" stroke-width="1.8" fill="none"/></svg>Help to grow your business</li>
      <li><svg viewBox="0 0 16 16"><circle cx="8" cy="8" r="8" fill="var(--red)"/><path d="M4.5 8.3l2.4 2.3 4.6-4.8" stroke="#fff" stroke-width="1.8" fill="none"/></svg>Talk directly to your accountant, the person<br>who knows you</li>
      <li><svg viewBox="0 0 16 16"><circle cx="8" cy="8" r="8" fill="var(--red)"/><path d="M4.5 8.3l2.4 2.3 4.6-4.8" stroke="#fff" stroke-width="1.8" fill="none"/></svg>Small business &amp; Primary Producer<br>Specialists</li>
    </ul>
    <p class="back__tagline">+ More.......Tallywell Group.<br>You're more than a number<br>with us.</p>
    <p class="team"><span class="role">Director:</span> Gordon Pellew CPA<br><span class="role">Associate:</span> Soraya Finch CPA</p>
    <p class="back__phone">
      <svg width="26" height="26" viewBox="0 0 24 24"><path fill="var(--red)" d="M6.6 10.8c1.4 2.8 3.8 5.1 6.6 6.6l2.2-2.2c.3-.3.7-.4 1-.2 1.1.4 2.3.6 3.6.6.6 0 1 .4 1 1V20c0 .6-.4 1-1 1C10.6 21 3 13.4 3 4c0-.6.4-1 1-1h3.5c.6 0 1 .4 1 1 0 1.3.2 2.5.6 3.6.1.3 0 .7-.2 1z"/></svg>
      (07) 4519 2386
    </p>
    <p class="contact-line">
      <svg width="18" height="20" viewBox="0 0 24 24"><path fill="var(--red)" d="M12 2a7 7 0 0 0-7 7c0 5.2 7 13 7 13s7-7.8 7-13a7 7 0 0 0-7-7zm0 9.5A2.5 2.5 0 1 1 12 6.5a2.5 2.5 0 0 1 0 5z"/></svg>
      PO Box 827 Wandarra Qld 4417
    </p>
    <p class="web back__web">
      <svg width="16" height="16" viewBox="0 0 24 24" fill="none" stroke="var(--red)" stroke-width="2"><circle cx="12" cy="12" r="10"/><path d="M2 12h20M12 2c3 3 3 17 0 20M12 2c-3 3-3 17 0 20"/></svg>
      www.ledgerbrightco.com.au
    </p>
  </div>
</section>

</body>
</html>
```